business card for real estate company
Coastway Summit Realty
Simple
Dimitri Lavrentis
Broker / Owner
118 Alder Lane
Larkfield, CV 02417
dimitri@coastsummitrealty.com
www.coastsummitrealty.com
clean professional look that people wont have a hard time reading. Thank you in advance for your designs.

```html
<!DOCTYPE html>
<html lang="en">
<head>
<meta charset="utf-8">
<title>Coastway Summit Realty — Business Card</title>
<link rel="stylesheet" href="https://fonts.googleapis.com/css2?family=Cinzel:wght@400;600&display=swap">
<style>
  :root {
    --page-bg: #e9e9ea;
    --card-white: #ffffff;
    --brand-navy: #1c2f5e;
    --band-blue: #1f3fb4;
    --band-blue-light: #2f56d6;
    --band-blue-dark: #16308f;
    --rule-grey: #b9bcc4;
    --text-white: #ffffff;
  }
  * { box-sizing: border-box; margin: 0; padding: 0; }
  html, body {
    width: 1200px; height: 900px; overflow: hidden;
    background: var(--page-bg);
    font-family: "Cinzel", Georgia, serif;
  }
  .canvas {
    position: relative; width: 1200px; height: 900px;
    display: flex; align-items: center; justify-content: center;
  }
  .business-card {
    position: relative; width: 1050px; height: 600px;
    background: var(--card-white);
    box-shadow: 0 10px 30px rgba(0,0,0,0.18);
    overflow: hidden;
  }
  .brand {
    position: absolute; top: 130px; left: 0; right: 0;
    display: flex; align-items: center; justify-content: center; gap: 22px;
  }
  .brand-square {
    width: 64px; height: 64px; background: var(--brand-navy);
  }
  .brand-name {
    color: var(--brand-navy); font-weight: 600; font-size: 44px;
    letter-spacing: 1px; font-variant: small-caps;
  }
  .band-rule {
    position: absolute; left: 0; right: 0; height: 6px; background: var(--rule-grey);
  }
  .band-rule.top { top: 296px; }
  .band-rule.bottom { top: 506px; }
  .contact-band {
    position: absolute; left: 0; right: 0; top: 304px; height: 200px;
    background: linear-gradient(180deg, var(--band-blue-light) 0%, var(--band-blue) 45%, var(--band-blue-dark) 100%);
    color: var(--text-white);
  }
  .contact-list {
    position: absolute; left: 30px; top: 12px; list-style: none;
  }
  .contact-list li {
    display: flex; align-items: center; gap: 12px;
    height: 29px; font-size: 19px; letter-spacing: 0.5px;
  }
  .contact-list svg { width: 18px; height: 18px; flex: none; }
  .contact-list .no-icon { padding-left: 30px; }
  .person {
    position: absolute; right: 34px; top: 52px; text-align: right;
  }
  .person-name { font-size: 22px; letter-spacing: 0.5px; }
  .person-title { font-size: 15px; letter-spacing: 1px; margin-top: 2px; }
</style>
</head>
<body>
<main class="canvas">
  <section class="business-card">
    <div class="brand">
      <span class="brand-square"></span>
      <span class="brand-name">Coastway Summit Realty</span>
    </div>
    <div class="band-rule top"></div>
    <div class="contact-band">
      <ul class="contact-list">
        <li>
          <svg viewBox="0 0 20 20"><circle cx="10" cy="10" r="10" fill="#fff"/><path d="M5 11 L10 6 L15 11 V15 H5 Z" fill="#1f3fb4"/></svg>
          118 Alder Lane
        </li>
        <li class="no-icon">Larkfield, CV 02417</li>
        <li>
          <svg viewBox="0 0 20 20"><circle cx="10" cy="10" r="10" fill="#fff"/><path d="M7 5 L9 5 L10 8 L8.5 9 Q9.5 11 11 11.5 L12 10 L15 11 L15 13 Q13 15 10 13 Q6.5 11 5.5 8 Q5 6 7 5 Z" fill="#1f3fb4"/></svg>
          (555) 706-0142
        </li>
        <li>
          <svg viewBox="0 0 20 20"><circle cx="10" cy="10" r="10" fill="#fff"/><rect x="6" y="4" width="8" height="12" rx="1.5" fill="#1f3fb4"/><circle cx="10" cy="14" r="0.9" fill="#fff"/></svg>
          (555) 577-0187
        </li>
        <li>
          <svg viewBox="0 0 20 20"><circle cx="10" cy="10" r="10" fill="#fff"/><rect x="5" y="6.5" width="10" height="7" fill="#1f3fb4"/><path d="M5 6.5 L10 10.5 L15 6.5" stroke="#fff" stroke-width="1" fill="none"/></svg>
          dimitri@coastsummitrealty.com
        </li>
        <li>
          <svg viewBox="0 0 20 20"><circle cx="10" cy="10" r="10" fill="#fff"/><circle cx="10" cy="10" r="5.5" fill="none" stroke="#1f3fb4" stroke-width="1.4"/><path d="M4.5 10 H15.5 M10 4.5 V15.5" stroke="#1f3fb4" stroke-width="1.2"/></svg>
          www.coastsummitrealty.com
        </li>
      </ul>
      <div class="person">
        <p class="person-name">Dimitri Lavrentis</p>
        <p class="person-title">Broker / Owner</p>
      </div>
    </div>
    <div class="band-rule bottom"></div>
  </section>
</main>
</body>
</html>
```